Dane Moro films- wedding and event films company website. DESKTOP AND MOBILE

We need a website for a high-end wedding and event film production company. Looking for a very modern and elegant design. my old website is www.danemorofilms.example

I like the "white/black/rose gold" color scheme of my logo.

really looking for a sleek modern design the breaths professional and artistic.

Target Market(s)

wedding and event films.

Industry/Entity Type

Film Production

Number of Pages Required

5+ page

Colors

Designer to choose colors to be used in the design.

Requirements
Must have
• website name will be www.danemorofilms.example
• tagline is "CINEMATIC STORIES ABOUT YOU"
• sections: HOME, CONTACT, ABOUT, FILMS, BLOG
• You can see my old website at danemorofilms.example
• Website about section:
• Dane Moro Films was Established with the basis of truly cinematic and artistic films in mind. Dane and his team routinely travel the globe documenting weddings and events for high profile clients and discerning couples. Dane was born and raised in Maui Hawaii and has a unique approach to his films that embody the essence of a Hollywood film. Dane has spent the last 10 years traveling the world documenting corporate events and weddings with multiple Award winning production companies. In 2017 Dane decided to establish his own brand “Dane Moro films” that will take everything he has learned with his past experiences and push it to the next level. Aside from his personal achievements, Dane is extremely passionate about his craft and always looks forward to handcrafting beautiful wedding/event films for his clients. The style of work is non-traditional and the day of filming is extremely unobtrusive (as we are looking for natural-candid/ raw emotions).
• If you are looking for the best price in town, we are probably not the best option, but if you’re looking for the best quality and peace of mind on your wedding day, then you’re in the right place. Dane Moro Films is a boutique studio that only accepts a limited number of assignments per year. Inquire early to ensure availability.
• LINKS TO REELHUB VIDEOS THAT WILL BE IN THE "FILMS' SECTION.
• BRENT FILM TRAILER - https://clipvault.example/418205736
• BRENT FEATURE FILM - https://clipvault.example/527910384
• NORA AND PAUL'S WEDDING - https://clipvault.example/649382015
• DRONE DEMO REEL - https://clipvault.example/751046923
• WEDDING INDUSTRY EVENT PARTY - https://clipvault.example/862937104/7a2d9c3e8b
• images that you can use on site are here: https://maribelortegaphotos.picvault.example/gallery/ruth&glen/
• password is: meadow

```html
<!DOCTYPE html>
<html lang="en">
<head>
<meta charset="utf-8">
<title>Contact — Dane Moro Films</title>
<link rel="stylesheet" href="https://fonts.googleapis.com/css2?family=Bebas+Neue&family=Roboto+Condensed:wght@400&family=Open+Sans:wght@300;400;700&family=Montserrat:wght@400;700&display=swap">
<style>
  :root {
    --ink-white: #ffffff;
    --rose-gold: #d9a071;
    --rose-gold-line: #8a6443;
    --body-bg: #282828;
    --panel-bg: #2b2b2b;
    --footer-bg: #222222;
    --muted: #6a6a6a;
    --placeholder: #7a7a7a;
    --icon-grey: #8c8c8c;
  }
  * { box-sizing: border-box; margin: 0; padding: 0; }
  html, body { width: 1200px; height: 1140px; overflow: hidden; background: var(--body-bg); }
  body { position: relative; font-family: "Open Sans", sans-serif; color: var(--ink-white); }

  .hero {
    position: absolute; left: 0; top: 0; width: 1200px; height: 623px;
  }
  .hero-photo {
    position: absolute; inset: 0;
    background:
      radial-gradient(ellipse 420px 120px at 860px 345px, rgba(150,95,45,0.55), rgba(0,0,0,0) 70%),
      linear-gradient(180deg, #3f3f41 0%, #4a4745 35%, #5a4b3f 52%, #201c19 57%, #141312 75%, #0f0f0f 100%);
  }
  .site-nav {
    position: absolute; top: 36px; right: 87px;
    display: flex; gap: 0;
  }
  .site-nav a {
    font-family: "Roboto Condensed", sans-serif; font-size: 14px; letter-spacing: 1px;
    color: var(--ink-white); text-decoration: none; margin-left: 48px;
  }
  .site-nav a.is-active { color: var(--rose-gold); }

  .brand {
    position: absolute; display: flex; align-items: center; gap: 6px;
    font-family: "Montserrat", sans-serif; font-weight: 400; font-size: 10px; letter-spacing: 0.5px;
  }
  .brand-mark { width: 8px; height: 8px; background: currentColor; }
  .brand--header { left: 87px; top: 54px; color: var(--ink-white); }
  .brand--footer { left: 556px; top: 1093px; color: var(--ink-white); }

  .hero-title {
    position: absolute; left: 0; width: 1200px; top: 280px; text-align: center;
    font-family: "Bebas Neue", sans-serif; font-size: 56px; letter-spacing: 4px; line-height: 1;
  }

  .intro {
    position: absolute; left: 87px; top: 695px;
    font-size: 14px; letter-spacing: 1px; line-height: 16px;
  }
  .intro strong { font-weight: 700; }
  .intro .contact-lines { margin-top: 16px; }

  .contact-panel {
    position: absolute; left: 600px; top: 676px; width: 512px; height: 309px;
    background: var(--panel-bg);
  }
  .contact-panel h2 {
    position: absolute; left: 27px; top: 24px;
    font-family: "Montserrat", sans-serif; font-weight: 700; font-size: 16px; letter-spacing: 2px;
  }
  .field {
    position: absolute; border: 1px solid var(--rose-gold-line); background: transparent;
    font-family: "Open Sans", sans-serif; font-size: 14px; letter-spacing: 1px;
    color: var(--placeholder); padding: 7px 10px;
  }
  .field--first { left: 27px; top: 60px; width: 226px; height: 31px; }
  .field--last  { left: 259px; top: 60px; width: 227px; height: 31px; }
  .field--email { left: 27px; top: 97px; width: 458px; height: 31px; }
  .field--message { left: 27px; top: 135px; width: 458px; height: 109px; }
  .send-button {
    position: absolute; left: 27px; top: 250px; width: 100px; height: 32px;
    background: var(--rose-gold); color: #2a2a2a; border: none;
    font-family: "Open Sans", sans-serif; font-size: 14px; letter-spacing: 1px;
    display: flex; align-items: center; justify-content: center;
  }

  .site-footer {
    position: absolute; left: 0; top: 1037px; width: 1200px; height: 103px;
    background: var(--footer-bg);
  }
  .copyright {
    position: absolute; left: 87px; top: 1078px;
    font-family: "Open Sans", sans-serif; font-weight: 300; font-size: 14px; color: var(--muted);
  }
  .social {
    position: absolute; top: 1080px; right: 87px; display: flex; gap: 28px;
  }
  .social a {
    font-family: "Open Sans", sans-serif; font-size: 12px; color: var(--icon-grey); text-decoration: none;
  }
</style>
</head>
<body>
  <header class="hero">
    <div class="hero-photo" role="img" aria-label="Camera on a tripod silhouetted against a mountain sunset"></div>
    <div class="brand brand--header"><span class="brand-mark"></span>DANE MORO FILMS</div>
    <nav class="site-nav">
      <a href="#">HOME</a>
      <a href="#" class="is-active">ABOUT</a>
      <a href="#">FILMS</a>
      <a href="#">CONTACT</a>
      <a href="#">BLOG</a>
    </nav>
    <h1 class="hero-title">CONTACT</h1>
  </header>

  <main>
    <section class="intro">
      <p><strong>For pricing and availability please contact Dane:</strong><br>We are available to travel anywhere!</p>
      <p class="contact-lines">E:&nbsp; dane@danemorofilms.example<br>P:&nbsp; 555-014-7129</p>
    </section>

    <section class="contact-panel">
      <h2>CONTACT</h2>
      <div class="field field--first">Fist Name</div>
      <div class="field field--last">Last Name</div>
      <div class="field field--email">Email</div>
      <div class="field field--message">Content</div>
      <div class="send-button">Send</div>
    </section>
  </main>

  <footer class="site-footer"></footer>
  <p class="copyright">Copyright by DANE MORO&nbsp; © 2015</p>
  <div class="brand brand--footer"><span class="brand-mark" style="background: var(--rose-gold);"></span>DANE MORO FILMS</div>
  <nav class="social">
    <a href="#">Friendly</a>
    <a href="#">Chirper</a>
    <a href="#">Reelhub</a>
  </nav>
</body>
</html>
```